Business cards for a naturopathic day clinic for stem cell therapy

We need a basic design for a day clinic, that offers stem cell therapies for Lyme therapy and other severe chronic illnesses.
Our name is "Casa velorìn", which can be translated into "Manor Velorbloom". We are a couple of naturopaths working along side physiotherapists and osteopaths, yoga teachers and massage therapists. I attached our logo.

```html
<!DOCTYPE html>
<html lang="en">
<head>
<meta charset="utf-8">
<title>Casa velorìn — Business Cards</title>
<link rel="stylesheet" href="https://fonts.googleapis.com/css2?family=Montserrat:wght@300;400;500;700&display=swap">
<style>
  :root {
    --backdrop: #b9b9b9;
    --backdrop-light: #dedede;
    --card-white: #ffffff;
    --leaf-green: #a9bf45;
    --bark-brown: #86705f;
    --ink: #4a423c;
  }
  * { box-sizing: border-box; margin: 0; padding: 0; }
  html, body { width: 1200px; height: 800px; overflow: hidden; }
  body {
    background: radial-gradient(ellipse at 20% 10%, var(--backdrop-light), var(--backdrop) 75%);
    font-family: "Montserrat", sans-serif;
    position: relative;
  }
  .card {
    position: absolute;
    width: 520px;
    height: 300px;
    border-radius: 18px;
    overflow: hidden;
    box-shadow: 0 14px 30px rgba(0,0,0,0.22);
  }
  .card--front { left: 70px; top: 100px; background: var(--card-white); }
  .card--back { left: 610px; top: 400px; background: var(--bark-brown); }

  .front-band { position: absolute; inset: 0; }

  .brand {
    position: absolute;
    display: flex;
    align-items: center;
    gap: 12px;
  }
  .brand__dot { border-radius: 50%; flex: none; }
  .brand__name { font-weight: 300; white-space: nowrap; line-height: 1; }

  .card--front .brand { left: 24px; top: 108px; }
  .card--front .brand__dot { width: 30px; height: 30px; background: var(--leaf-green); }
  .card--front .brand__name { font-size: 28px; color: var(--ink); }

  .divider {
    position: absolute;
    left: 252px;
    top: 44px;
    width: 1px;
    height: 140px;
    background: var(--leaf-green);
  }

  .contact {
    position: absolute;
    left: 268px;
    top: 34px;
    color: var(--ink);
    font-size: 11px;
    line-height: 1.45;
  }
  .contact__name { font-size: 19px; font-weight: 700; color: var(--leaf-green); line-height: 1.1; }
  .contact__role { font-size: 12px; font-weight: 500; color: var(--bark-brown); margin-bottom: 8px; }
  .contact__address { margin-bottom: 6px; }
  .contact__list { list-style: none; }
  .contact__list li { display: flex; align-items: center; gap: 7px; white-space: nowrap; }
  .contact__list svg { width: 10px; height: 10px; fill: var(--bark-brown); flex: none; }

  .web-address {
    position: absolute;
    left: 150px;
    top: 264px;
    color: var(--card-white);
    font-size: 12px;
    line-height: 1;
    white-space: nowrap;
    transform: rotate(-3deg);
    transform-origin: left center;
  }
  .web-address strong { font-weight: 700; }

  .card--back .brand { left: 50%; top: 50%; transform: translate(-50%, -50%); gap: 16px; }
  .card--back .brand__dot { width: 44px; height: 44px; background: var(--leaf-green); }
  .card--back .brand__name { font-size: 48px; color: var(--leaf-green); }
</style>
</head>
<body>

  <section class="card card--front" aria-label="Business card front">
    <svg class="front-band" viewBox="0 0 520 300" width="520" height="300" aria-hidden="true">
      <path d="M0,300 L0,290 Q240,210 520,252 L520,300 Z" fill="var(--leaf-green)"/>
      <path d="M0,282 Q240,202 520,244" fill="none" stroke="var(--bark-brown)" stroke-width="3"/>
    </svg>

    <div class="brand">
      <span class="brand__dot"></span>
      <span class="brand__name">Casa velorìn</span>
    </div>

    <div class="divider"></div>

    <div class="contact">
      <p class="contact__name">Elena Marris</p>
      <p class="contact__role">President</p>
      <p class="contact__address">412 Linden Row<br>Fairbanks, Alaska 99701</p>
      <ul class="contact__list">
        <li><svg viewBox="0 0 10 10"><path d="M2 0.5 L3.8 2.6 L2.8 3.8 Q4 6 6.2 7.2 L7.4 6.2 L9.5 8 L8.2 9.5 Q3.5 9 0.5 1.8 Z"/></svg>555-204-7731</li>
        <li><svg viewBox="0 0 10 10"><path d="M1 1 H9 V9 H1 Z M2.2 2.2 V7.8 H7.8 V2.2 Z" fill-rule="evenodd"/></svg>555-318-4026</li>
        <li><svg viewBox="0 0 10 10"><rect x="2.5" y="0.5" width="5" height="9" rx="1"/></svg>555-471-9083</li>
        <li><svg viewBox="0 0 10 10"><path d="M0.5 2 H9.5 V8.5 H0.5 Z M1.2 2.6 L5 5.6 L8.8 2.6" fill-rule="evenodd"/></svg>hello@casavelorin.com</li>
      </ul>
    </div>

    <p class="web-address">www.<strong>casavelorin</strong>.com</p>
  </section>

  <section class="card card--back" aria-label="Business card back">
    <div class="brand">
      <span class="brand__dot"></span>
      <span class="brand__name">Casa velorìn</span>
    </div>
  </section>

</body>
</html>
```